Venue Booking Site

I would like a venue directory and booking website designed. The idea is that end users will come to the site to find venues for weddings, parties, events etc. They will be able to find the venue based on many criteria, the most important ones are availability and location - they will be able to see in real time which venues are available for the desired dates and areas.

Venues will be able to use the website as a reservation management tool, receive payments for bookings through the site and be able to manage bookings on the go. This will be made into an app. It needs to be developed in bootstrap. Brand name to be used: Pinevault. Venue, place and space bookings.

Target audience - end users - anyone who is looking for a venue. For Community members it will provide an easy way to find a suitable venue
Outline what dates and times the venue is available
Outline costs involved in booking the venue
Search via many other criteria
It will allow the customer to book and pay for the venue online in one smooth process

Clients: Venue managers - particularly focussing on not for profit businesses eg, GPWs, community hall managers, small business managers. These people typically use paper based systems yet and do not use websites so it needs to be very user friendly. Future growth to restaurants, pubs, event venues who have a stronger familiarity with computers and who might already use their own booking management tool - so this needs to be able to link in with their system.

What need will this meet for venue managers:
This tool provides venues with greater visibility, promotion and advertising of their venue
This allows more customers to find them and book with them
This tool will be offered to not-for-profit venue managers for free to better connect them to the community
This means greater profit for these community venues
This means more revenue and jobs created in these communities

Sample of the layout / contents attached. This is not a complete site map as yet as it is a work in progress for final pages.

Industry/Entity Type

Small Business

Number of Pages Required

5+ page

Font styles to use
Sans Serif

Colors
eb2027

Requirements
Must have
• This is a psd file only - one template for each different section, home page, search page, detailed page view, admin back end
Should not have
• does not need to be coded.
• Note, the lantern quay logo jpeg files were files we were toying with using for this project- but I am happy to use the main pinevault logo- I will let you decide.

```html
<!DOCTYPE html>
<html lang="en">
<head>
<meta charset="utf-8">
<title>Pinevault – Venue Booking</title>
<link rel="stylesheet" href="https://fonts.googleapis.com/css2?family=Montserrat:wght@400;500;600;700&family=Open+Sans:ital,wght@0,400;0,600;0,700;1,400&display=swap">
<style>
  :root {
    --red: #eb2027;
    --red-dark: #d41a20;
    --blue: #1e9be0;
    --ink: #2f2f2f;
    --text: #555;
    --line: #e1e1e1;
    --panel-grey: #ececec;
    --section-grey: #f2f2f2;
    --footer: #333333;
    --footer-deep: #232323;
    --footer-text: #c9c9c9;
    --white: #fff;
  }
  * { box-sizing: border-box; margin: 0; padding: 0; }
  a { text-decoration: none; color: inherit; }
  html, body { width: 1200px; height: 2188px; overflow: hidden; }
  body { position: relative; background: var(--white); font-family: "Open Sans", Arial, sans-serif; color: var(--text); }
  .abs { position: absolute; }

  /* Top utility bar */
  .utility-bar { position: absolute; left: 0; top: 0; width: 1200px; height: 33px; background: var(--white); font-size: 11px; color: #444; }
  .utility-item { position: absolute; top: 0; height: 33px; display: flex; align-items: center; gap: 6px; padding: 0 10px; border-left: 1px solid #e4e4e4; }
  .utility-item svg { width: 11px; height: 11px; }
  .search-toggle { position: absolute; left: 888px; top: 0; width: 37px; height: 33px; display: flex; align-items: center; justify-content: center; border-left: 1px solid #e4e4e4; }
  .list-venue { position: absolute; left: 925px; top: 0; width: 142px; height: 33px; background: var(--blue); color: var(--white); font-family: "Montserrat", sans-serif; font-weight: 600; font-size: 13px; display: flex; align-items: center; justify-content: center; gap: 10px; }

  /* Main navigation */
  .main-nav { position: absolute; left: 0; top: 33px; width: 1200px; height: 95px; background: var(--red); }
  .nav-link { position: absolute; top: 33px; height: 29px; line-height: 29px; font-family: "Montserrat", sans-serif; font-size: 16px; font-weight: 500; color: var(--white); }
  .nav-link.is-active { background: var(--white); color: var(--red); padding: 0 14px; }

  .brand { position: absolute; left: 131px; top: 0; width: 172px; height: 124px; background: var(--white); box-shadow: 0 2px 6px rgba(0,0,0,.18); z-index: 5; text-align: center; }
  .brand-name { display: block; margin-top: 34px; font-family: "Montserrat", sans-serif; font-weight: 700; font-size: 29px; color: var(--red); line-height: 1; }
  .brand-tag { display: block; margin-top: 12px; font-size: 12px; color: #333; }

  /* Map area */
  .map-area { position: absolute; left: 0; top: 128px; width: 1200px; height: 465px; background: linear-gradient(160deg, #e9e5dc 0%, #e3dfd5 55%, #ece8df 100%); }
  .map-card { position: absolute; left: 573px; top: 98px; width: 281px; height: 117px; background: var(--white); box-shadow: 0 2px 6px rgba(0,0,0,.2); }
  .map-card::before { content: ""; position: absolute; left: -10px; top: 48px; border: 10px solid transparent; border-left: 0; border-right-color: var(--white); }
  .map-card-photo { position: absolute; left: 14px; top: 15px; width: 106px; height: 88px; background: linear-gradient(135deg, #8fb07a, #d9ddd3 55%, #6f8d5e); }
  .map-card-title { position: absolute; left: 133px; top: 12px; font-family: "Montserrat", sans-serif; font-weight: 700; font-size: 16px; color: var(--red); white-space: nowrap; }
  .map-card-sub { position: absolute; left: 133px; top: 36px; font-size: 10.5px; color: #555; }
  .map-card-stars { position: absolute; left: 133px; top: 54px; }
  .map-card-text { position: absolute; left: 133px; top: 72px; width: 135px; font-size: 10.5px; line-height: 15px; color: #666; }
  .zoom { position: absolute; left: 1156px; top: 355px; width: 23px; background: var(--white); box-shadow: 0 1px 3px rgba(0,0,0,.3); }
  .zoom span { display: block; height: 26px; text-align: center; line-height: 25px; font-size: 17px; color: #555; }
  .zoom span + span { border-top: 1px solid #ddd; }

  /* Search panel */
  .search-panel { position: absolute; left: 131px; top: 580px; width: 938px; height: 210px; background: linear-gradient(180deg, #fff 0%, #fff 55%, #efefef 100%); box-shadow: 0 -2px 8px rgba(0,0,0,.12); z-index: 3; }
  .search-group { position: absolute; top: 28px; }
  .search-divider { position: absolute; top: 28px; width: 1px; height: 112px; background: var(--line); }
  .step-head { display: flex; align-items: center; gap: 10px; font-family: "Montserrat", sans-serif; font-weight: 600; font-size: 18px; color: var(--ink); }
  .step-num { width: 23px; height: 23px; background: var(--blue); color: var(--white); font-size: 11px; display: flex; align-items: center; justify-content: center; font-weight: 600; }
  .field-label { font-size: 11.5px; color: #444; }
  .checkbox { position: absolute; display: flex; align-items: center; gap: 10px; font-size: 11.5px; color: #444; }
  .checkbox i { width: 13px; height: 13px; background: #dadada; border: 1px solid #cdcdcd; }
  .input { position: absolute; height: 28px; background: #e9e9e9; border: 1px solid #dcdcdc; font-size: 11px; color: #777; display: flex; align-items: center; padding: 0 8px; gap: 6px; }
  .input.date { justify-content: space-between; }
  .search-button { position: absolute; left: 385px; top: 146px; width: 166px; height: 40px; background: var(--red); color: var(--white); font-family: "Montserrat", sans-serif; font-weight: 600; font-size: 17px; display: flex; align-items: center; justify-content: center; box-shadow: 0 2px 0 var(--red-dark); }

  /* Top venues */
  .top-venues { position: absolute; left: 0; top: 812px; width: 1200px; height: 528px; background: var(--section-grey); }
  .section-title { position: absolute; left: 0; width: 1200px; text-align: center; font-family: "Montserrat", sans-serif; font-weight: 600; color: var(--ink); }
  .top-venues .section-title { top: 30px; font-size: 30px; }
  .title-rule { position: absolute; top: 50px; width: 183px; height: 1px; background: #c9c9c9; }
  .venue-card { position: absolute; top: 96px; width: 215px; height: 402px; background: var(--white); border: 1px solid #e2e2e2; box-shadow: 0 1px 3px rgba(0,0,0,.08); }
  .venue-photo { position: absolute; left: 9px; top: 9px; width: 197px; height: 124px; }
  .venue-name { position: absolute; left: 12px; top: 146px; font-family: "Montserrat", sans-serif; font-weight: 600; font-size: 16px; color: var(--ink); white-space: nowrap; }
  .venue-tagline { position: absolute; left: 12px; top: 174px; font-size: 12px; color: #444; }
  .venue-rating { position: absolute; left: 12px; top: 198px; width: 191px; display: flex; justify-content: space-between; align-items: center; }
  .venue-score { display: flex; align-items: center; gap: 5px; font-size: 11px; color: #666; }
  .price-bar { position: absolute; left: 9px; top: 226px; width: 197px; height: 28px; background: var(--panel-grey); display: flex; align-items: center; justify-content: space-between; padding: 0 8px; font-size: 11.5px; color: #555; }
  .price { font-family: "Montserrat", sans-serif; font-weight: 700; font-size: 18px; color: var(--red); }
  .venue-desc { position: absolute; left: 12px; top: 270px; width: 188px; font-size: 11.5px; line-height: 17.5px; color: #555; }
  .book-now { position: absolute; left: 12px; top: 354px; width: 124px; height: 32px; background: var(--red); color: var(--white); font-family: "Montserrat", sans-serif; font-weight: 600; font-size: 14px; display: flex; align-items: center; justify-content: center; }

  /* Why section */
  .why { position: absolute; left: 0; top: 1340px; width: 1200px; height: 497px; background: var(--white); }
  .why .section-title { top: 40px; font-size: 28px; }
  .feature { position: absolute; width: 215px; }
  .feature-title { text-align: center; font-family: "Montserrat", sans-serif; font-weight: 500; font-size: 17px; color: var(--red); height: 24px; }
  .feature-box { position: relative; height: 113px; background: var(--panel-grey); padding: 30px 14px 0; font-size: 11.5px; line-height: 18px; color: #555; }
  .feature-box::after { content: ""; position: absolute; right: 0; top: 0; border-style: solid; border-width: 0 16px 16px 0; border-color: transparent var(--white) transparent transparent; }
  .feature-box::before { content: ""; position: absolute; right: 0; top: 0; width: 16px; height: 16px; background: #d9d9d9; clip-path: polygon(0 0, 0 100%, 100% 100%); }

  /* Newsletter */
  .newsletter { position: absolute; left: 0; top: 1837px; width: 1200px; height: 84px; background: var(--red); }
  .newsletter-title { position: absolute; left: 131px; top: 13px; font-family: "Montserrat", sans-serif; font-weight: 600; font-size: 27px; color: var(--white); }
  .newsletter-sub { position: absolute; left: 131px; top: 52px; font-size: 14px; color: #ffe3e4; }
  .newsletter-input { position: absolute; left: 604px; top: 20px; width: 326px; height: 46px; background: var(--white); display: flex; align-items: center; gap: 12px; padding: 0 16px; font-style: italic; font-size: 15px; color: #aaa; }
  .newsletter-button { position: absolute; left: 930px; top: 20px; width: 139px; height: 46px; background: #222; color: var(--white); font-family: "Montserrat", sans-serif; font-weight: 600; font-size: 19px; display: flex; align-items: center; justify-content: center; }

  /* Footer */
  .site-footer { position: absolute; left: 0; top: 1921px; width: 1200px; height: 224px; background: var(--footer); color: var(--footer-text); }
  .footer-col { position: absolute; top: 28px; }
  .footer-heading { font-family: "Montserrat", sans-serif; font-weight: 500; font-size: 16px; color: #eee; letter-spacing: .5px; margin-bottom: 18px; }
  .footer-links { list-style: none; font-size: 12.5px; }
  .footer-links li { height: 27.4px; display: flex; align-items: center; gap: 12px; }
  .footer-links li::before { content: "→"; color: #aaa; font-size: 12px; }
  .footer-divider { position: absolute; top: 58px; width: 1px; height: 146px; background: #474747; }
  .contact-line { display: flex; align-items: center; gap: 14px; font-size: 12.5px; height: 31px; }
  .contact-line svg { width: 14px; height: 14px; }
  .contact-name { font-weight: 700; font-size: 12.5px; color: #e5e5e5; height: 20px; }
  .social-line { display: flex; align-items: center; gap: 10px; height: 33px; font-size: 12.5px; }
  .social-dot { width: 20px; height: 20px; border-radius: 50%; background: #5a5a5a; }
  .footer-bottom { position: absolute; left: 0; top: 2145px; width: 1200px; height: 43px; background: var(--footer-deep); text-align: center; line-height: 43px; font-size: 12px; color: #aaa; }
</style>
</head>
<body>

<svg width="0" height="0" style="position:absolute">
  <defs><path id="s" d="M6 0l1.8 3.9 4.2.4-3.2 2.8 1 4.1L6 9.1 2.2 11.2l1-4.1L0 4.3l4.2-.4z"/></defs>
</svg>

<!-- Utility bar -->
<div class="utility-bar">
  <div class="utility-item" style="left:492px;">
    <svg viewBox="0 0 12 12"><rect x="3" y="0.5" width="6" height="11" rx="1" fill="#555"/><rect x="4" y="2" width="4" height="7" fill="#fff"/></svg>
    03 5550 1427
  </div>
  <div class="utility-item" style="left:612px;">
    <svg viewBox="0 0 12 12"><rect x="2" y="5" width="8" height="7" fill="#555"/><path d="M3.5 5V3.5a2.5 2.5 0 0 1 5 0V5" stroke="#555" stroke-width="1.4" fill="none"/></svg>
    Login
  </div>
  <div class="utility-item" style="left:682px;">
    <svg viewBox="0 0 12 12"><rect x="1" y="2" width="9" height="9" fill="none" stroke="#555" stroke-width="1.2"/><path d="M5 7l6-6" stroke="#555" stroke-width="1.4"/></svg>
    Sign Up
  </div>
  <div class="utility-item" style="left:760px; padding:0; width:1px;"></div>
  <div class="search-toggle">
    <svg width="13" height="13" viewBox="0 0 13 13"><circle cx="5.5" cy="5.5" r="4" stroke="#444" stroke-width="1.6" fill="none"/><path d="M8.5 8.5L12 12" stroke="#444" stroke-width="1.8"/></svg>
  </div>
  <div class="list-venue">List My Venue <span>›</span></div>
</div>

<!-- Brand -->
<a class="brand" href="#">
  <span class="brand-name">pinevault</span>
  <span class="brand-tag">Venue Booking</span>
</a>

<!-- Navigation -->
<nav class="main-nav">
  <a class="nav-link is-active" style="left:418px;">Home</a>
  <a class="nav-link" style="left:527px;">Venues</a>
  <a class="nav-link" style="left:620px;">News &amp; Offers</a>
  <a class="nav-link" style="left:773px;">Inspiration</a>
  <a class="nav-link" style="left:897px;">Contact</a>
  <a class="nav-link" style="left:1001px;">Faqs</a>
</nav>

<!-- Map -->
<div class="map-area">
  <div class="abs" style="inset:0;" role="img" aria-label="Street map of the coastal city area with photo markers for each venue location"></div>
  <div class="map-card">
    <div class="map-card-photo" role="img" aria-label="Photo of the Coral Reach venue exterior"></div>
    <div class="map-card-title">Coral Reach</div>
    <div class="map-card-sub">Lorem Ipsum</div>
    <svg class="map-card-stars" width="80" height="12" viewBox="0 0 80 12">
      <g fill="var(--blue)"><use href="#s"/><use href="#s" x="15"/><use href="#s" x="30"/></g>
      <g fill="#ccc"><use href="#s" x="45"/><use href="#s" x="60"/></g>
    </svg>
    <div class="map-card-text">There are many variations of passages</div>
  </div>
  <div class="zoom"><span>+</span><span>−</span></div>
</div>

<!-- Search panel -->
<form class="search-panel">
  <div class="search-group" style="left:20px;">
    <div class="step-head"><span class="step-num">01</span>What?</div>
  </div>
  <label class="checkbox" style="left:20px; top:66px;"><i></i>Hotel</label>
  <label class="checkbox" style="left:124px; top:66px;"><i></i>Self Catering</label>
  <label class="checkbox" style="left:20px; top:98px;"><i></i>Rent a Car</label>
  <label class="checkbox" style="left:124px; top:98px;"><i></i>Tour</label>

  <div class="search-divider" style="left:267px;"></div>

  <div class="search-group" style="left:299px;">
    <div class="step-head"><span class="step-num">02</span>Where?</div>
  </div>
  <div class="field-label abs" style="left:298px; top:64px;">Your Destination</div>
  <div class="input" style="left:298px; top:91px; width:184px;">
    <svg width="10" height="12" viewBox="0 0 10 12"><path d="M5 0a4 4 0 0 1 4 4c0 3-4 8-4 8S1 7 1 4a4 4 0 0 1 4-4z" fill="#999"/><circle cx="5" cy="4" r="1.5" fill="#e9e9e9"/></svg>
    City, Region
  </div>

  <div class="search-divider" style="left:509px;"></div>

  <div class="search-group" style="left:540px;">
    <div class="step-head"><span class="step-num">03</span>When?</div>
  </div>
  <div class="field-label abs" style="left:540px; top:64px;">Check in Date</div>
  <div class="field-label abs" style="left:659px; top:64px;">Check out Date</div>
  <div class="input date" style="left:540px; top:91px; width:100px;">01-10-2014
    <svg width="11" height="11" viewBox="0 0 11 11"><rect x=".5" y="1.5" width="10" height="9" fill="none" stroke="#777"/><path d="M.5 4h10M3 3l2 3 3-4" stroke="#777" fill="none"/></svg>
  </div>
  <div class="input date" style="left:659px; top:91px; width:100px;">01-10-2014
    <svg width="11" height="11" viewBox="0 0 11 11"><rect x=".5" y="1.5" width="10" height="9" fill="none" stroke="#777"/><path d="M.5 4h10M3 3l2 3 3-4" stroke="#777" fill="none"/></svg>
  </div>

  <div class="search-divider" style="left:790px;"></div>

  <div class="search-group" style="left:817px;">
    <div class="step-head"><span class="step-num">04</span>Who?</div>
  </div>
  <div class="field-label abs" style="left:817px; top:64px;">Rooms</div>
  <div class="input date" style="left:817px; top:91px; width:102px;">01
    <svg width="7" height="5" viewBox="0 0 7 5"><path d="M0 0h7L3.5 5z" fill="#777"/></svg>
  </div>

  <div class="search-button">SEARCH</div>
</form>

<!-- Top venues -->
<section class="top-venues">
  <div class="title-rule" style="left:319px;"></div>
  <h2 class="section-title">Top Venues</h2>
  <div class="title-rule" style="left:699px;"></div>

  <article class="venue-card" style="left:131px;">
    <div class="venue-photo" role="img" aria-label="Hotel lobby with chandelier" style="background:linear-gradient(135deg,#6b4a34,#d8b07c 50%,#7a2b33);"></div>
    <h3 class="venue-name">Seven Cedars Hotel</h3>
    <p class="venue-tagline">There are manyvaria</p>
    <div class="venue-rating">
      <svg width="80" height="12" viewBox="0 0 80 12"><g fill="var(--blue)"><use href="#s"/><use href="#s" x="15"/><use href="#s" x="30"/></g><g fill="#ccc"><use href="#s" x="45"/><use href="#s" x="60"/></g></svg>
      <span class="venue-score"><svg width="11" height="11" viewBox="0 0 11 11"><path d="M0 5h2v6H0zM3 5l3-5c1 0 1.5.8 1.2 2L7 4h3.2c.6 0 1 .6.8 1.2l-1.5 5.2c-.1.4-.5.6-.9.6H3z" fill="#aaa"/></svg>8/10</span>
    </div>
    <div class="price-bar"><span>Price Per Room &amp; night</span><span class="price">$80</span></div>
    <p class="venue-desc">Contrary to popular belief, Lorem Ipsum is not simply random text. It has roots in a piece of classical Latin literature from 45 BC</p>
    <a class="book-now">BOOK NOW</a>
  </article>

  <article class="venue-card" style="left:370px;">
    <div class="venue-photo" role="img" aria-label="Hotel exterior with pool at dusk" style="background:linear-gradient(180deg,#1d3a6b,#5a7fa8 55%,#c8a56a);"></div>
    <h3 class="venue-name">Coral Reach Hotel</h3>
    <p class="venue-tagline">There are manyvaria</p>
    <div class="venue-rating">
      <svg width="80" height="12" viewBox="0 0 80 12"><g fill="var(--blue)"><use href="#s"/><use href="#s" x="15"/><use href="#s" x="30"/></g><g fill="#ccc"><use href="#s" x="45"/><use href="#s" x="60"/></g></svg>
      <span class="venue-score"><svg width="11" height="11" viewBox="0 0 11 11"><path d="M0 5h2v6H0zM3 5l3-5c1 0 1.5.8 1.2 2L7 4h3.2c.6 0 1 .6.8 1.2l-1.5 5.2c-.1.4-.5.6-.9.6H3z" fill="#aaa"/></svg>8/10</span>
    </div>
    <div class="price-bar"><span>Price Per Room &amp; night</span><span class="price">$80</span></div>
    <p class="venue-desc">Contrary to popular belief, Lorem Ipsum is not simply random text. It has roots in a piece of classical Latin literature from 45 BC</p>
    <a class="book-now">BOOK NOW</a>
  </article>

  <article class="venue-card" style="left:609px;">
    <div class="venue-photo" role="img" aria-label="Hotel bedroom interior" style="background:linear-gradient(135deg,#7a5a34,#e2c48e 50%,#5b3b22);"></div>
    <h3 class="venue-name">Coral Reach</h3>
    <p class="venue-tagline">There are manyvaria</p>
    <div class="venue-rating">
      <svg width="80" height="12" viewBox="0 0 80 12"><g fill="var(--blue)"><use href="#s"/><use href="#s" x="15"/><use href="#s" x="30"/></g><g fill="#ccc"><use href="#s" x="45"/><use href="#s" x="60"/></g></svg>
      <span class="venue-score"><svg width="11" height="11" viewBox="0 0 11 11"><path d="M0 5h2v6H0zM3 5l3-5c1 0 1.5.8 1.2 2L7 4h3.2c.6 0 1 .6.8 1.2l-1.5 5.2c-.1.4-.5.6-.9.6H3z" fill="#aaa"/></svg>8/10</span>
    </div>
    <div class="price-bar"><span>Price Per Room &amp; night</span><span class="price">$80</span></div>
    <p class="venue-desc">Contrary to popular belief, Lorem Ipsum is not simply random text. It has roots in a piece of classical Latin literature from 45 BC</p>
    <a class="book-now">BOOK NOW</a>
  </article>

  <article class="venue-card" style="left:848px;">
    <div class="venue-photo" role="img" aria-label="Hotel building at night with street" style="background:linear-gradient(180deg,#2b4f8a,#6d86ad 50%,#4a4250);"></div>
    <h3 class="venue-name">Marlowe Hotel</h3>
    <p class="venue-tagline">There are manyvaria</p>
    <div class="venue-rating">
      <svg width="80" height="12" viewBox="0 0 80 12"><g fill="var(--blue)"><use href="#s"/><use href="#s" x="15"/><use href="#s" x="30"/></g><g fill="#ccc"><use href="#s" x="45"/><use href="#s" x="60"/></g></svg>
      <span class="venue-score"><svg width="11" height="11" viewBox="0 0 11 11"><path d="M0 5h2v6H0zM3 5l3-5c1 0 1.5.8 1.2 2L7 4h3.2c.6 0 1 .6.8 1.2l-1.5 5.2c-.1.4-.5.6-.9.6H3z" fill="#aaa"/></svg>8/10</span>
    </div>
    <div class="price-bar"><span>Price Per Room &amp; night</span><span class="price">$80</span></div>
    <p class="venue-desc">Contrary to popular belief, Lorem Ipsum is not simply random text. It has roots in a piece of classical Latin literature from 45 BC</p>
    <a class="book-now">BOOK NOW</a>
  </article>
</section>

<!-- Why book -->
<section class="why">
  <h2 class="section-title">Why Should You Book Your Venue Through Pinevault</h2>

  <div class="feature" style="left:131px; top:116px;"><h3 class="feature-title">Handpicked Hotels</h3><p class="feature-box">Contrary to popular belief, Lorem Ipsum is not simply random text. It has roots in a piece of classical Latin literature from 45 BC</p></div>
  <div class="feature" style="left:370px; top:116px;"><h3 class="feature-title">Detailed Descriptions</h3><p class="feature-box">Contrary to popular belief, Lorem Ipsum is not simply random text. It has roots in a piece of classical Latin literature from 45 BC</p></div>
  <div class="feature" style="left:609px; top:116px;"><h3 class="feature-title">Exclusive Knowledge</h3><p class="feature-box">Contrary to popular belief, Lorem Ipsum is not simply random text. It has roots in a piece of classical Latin literature from 45 BC</p></div>
  <div class="feature" style="left:848px; top:116px;"><h3 class="feature-title">Passionate Service</h3><p class="feature-box">Contrary to popular belief, Lorem Ipsum is not simply random text. It has roots in a piece of classical Latin literature from 45 BC</p></div>

  <div class="feature" style="left:131px; top:298px;"><h3 class="feature-title">Best Price Guarantee</h3><p class="feature-box">Contrary to popular belief, Lorem Ipsum is not simply random text. It has roots in a piece of classical Latin literature from 45 BC</p></div>
  <div class="feature" style="left:370px; top:298px;"><h3 class="feature-title">Secure Booking</h3><p class="feature-box">Contrary to popular belief, Lorem Ipsum is not simply random text. It has roots in a piece of classical Latin literature from 45 BC</p></div>
  <div class="feature" style="left:609px; top:298px;"><h3 class="feature-title">Benefits for Hoteliers</h3><p class="feature-box">Contrary to popular belief, Lorem Ipsum is not simply random text. It has roots in a piece of classical Latin literature from 45 BC</p></div>
  <div class="feature" style="left:848px; top:298px;"><h3 class="feature-title">Any Questions?</h3><p class="feature-box">Contrary to popular belief, Lorem Ipsum is not simply random text. It has roots in a piece of classical Latin literature from 45 BC</p></div>
</section>

<!-- Newsletter -->
<section class="newsletter">
  <h2 class="newsletter-title">Don't Miss Our Exclusive Offers</h2>
  <p class="newsletter-sub">There are many variations of passages</p>
  <div class="newsletter-input">
    <svg width="16" height="12" viewBox="0 0 16 12"><rect x=".5" y=".5" width="15" height="11" fill="none" stroke="#bbb"/><path d="M.5 .5L8 7l7.5-6.5" fill="none" stroke="#bbb"/></svg>
    Enter Your email here
  </div>
  <div class="newsletter-button">Signup</div>
</section>

<!-- Footer -->
<footer class="site-footer">
  <div class="footer-col" style="left:133px;">
    <h4 class="footer-heading">QUICK LINKS</h4>
    <ul class="footer-links"><li>Home</li><li>Venues</li><li>News &amp; Offers</li><li>Inspiration</li><li>Contact</li></ul>
  </div>
  <div class="footer-divider" style="left:295px;"></div>

  <div class="footer-col" style="left:347px;">
    <h4 class="footer-heading">COSTOMER SUPPORT</h4>
    <ul class="footer-links"><li>Faq</li><li>How do I make a reservation?</li><li>Payment Options</li><li>Booking tips</li></ul>
  </div>
  <div class="footer-divider" style="left:602px;"></div>

  <div class="footer-col" style="left:642px;">
    <h4 class="footer-heading">CONTACT INFO</h4>
    <div class="contact-name">Pinevault Bookings</div>
    <div class="contact-line"><svg viewBox="0 0 14 14"><path d="M7 0a5 5 0 0 1 5 5c0 4-5 9-5 9S2 9 2 5a5 5 0 0 1 5-5z" fill="#ccc"/><circle cx="7" cy="5" r="2" fill="#333"/></svg>12 Alder Crt Halloway VIC</div>
    <div class="contact-line"><svg viewBox="0 0 14 14"><path d="M3 0l3 3-2 2c1 2 3 4 5 5l2-2 3 3-2 3C6 14 0 8 0 2z" fill="#ccc"/></svg>03 5550 1427</div>
    <div class="contact-line"><svg viewBox="0 0 14 14"><rect x=".5" y="2.5" width="13" height="9" fill="none" stroke="#ccc"/><path d="M.5 2.5L7 8l6.5-5.5" fill="none" stroke="#ccc"/></svg>info@bookings.pinevault.com.au</div>
  </div>
  <div class="footer-divider" style="left:899px;"></div>

  <div class="footer-col" style="left:954px;">
    <h4 class="footer-heading">FOLLOW US</h4>
    <div class="social-line"><span class="social-dot"></span>Friendwall</div>
    <div class="social-line"><span class="social-dot"></span>Chirpline</div>
    <div class="social-line"><span class="social-dot"></span>Workweave</div>
    <div class="social-line"><span class="social-dot"></span>Circleplus</div>
  </div>
</footer>
<div class="footer-bottom">Copyright © 2014 Pinevault. All Rights Reserved.</div>

</body>
</html>
```